2957 Corliss Road Medical Centre

We are looking for a design for new medical clinic.
We are accepting new patients at this new medical centre grand opening. Walk-ins are welcome.
Our cardiac and vascular surgical specialists are department heads at Brenwood Vale Hospital, a leading teaching hospital in Toronto. These specialists will see cardiovascular consults are well as pre-surgical and post-surgical consultations and follow-ups.
Our lab is affiliated with several nuclear medicine clinics in the GTA.
Our Services Includes:
Family Practice
Cardiology Diagnostics
Cardiac & Vascular Surgical Consultation
Ultrasound & Vascular Testing
Open 6 days a week.
Ample Free Parking
Friendly Staffs

Target Market(s)

New Patients. Families of any age. Ethnic groups including Asians & Africans.

Industry/Entity Type

Medical

Font styles to use
Serif
Sans Serif
Decorative
Script
Other font styles liked:
• Arial calibri, verdana

Requirements
Must have
• Address:
• 2957 Corliss Road West
• Unit 418
• Scarborough, Ontario
• K7P 2H9
• Tel: (555) 384-2760
Nice to have
• Caring and inviting environment.
• Simple but classy.
• Standout colors.
Should not have
• Busy images. Aside from this, any ideas are welcome.

```html
<!DOCTYPE html>
<html lang="en">
<head>
<meta charset="utf-8">
<title>2957 Corliss Road Medical Centre – New Medical Clinic</title>
<link rel="stylesheet" href="https://fonts.googleapis.com/css2?family=Montserrat:wght@700;800&family=Noto+Sans:wght@400;700&family=Questrial&display=swap">
<style>
  :root {
    --teal: #1fb5c3;
    --teal-deep: #0f8f9b;
    --white: #ffffff;
    --ink: #111111;
    --paper: #f1f3f4;
    --band: #3b5050;
    --address: #2cc3cf;
  }
  html, body { margin: 0; padding: 0; overflow: hidden; }
  body { width: 928px; height: 1200px; background: var(--white); }
  .flyer {
    position: relative; width: 928px; height: 1200px; overflow: hidden;
    background: linear-gradient(180deg, #ffffff 0%, var(--paper) 55%, #e9eced 100%);
    font-family: "Noto Sans", Verdana, sans-serif; color: var(--ink);
  }
  .header-waves { position: absolute; left: 0; top: 0; width: 928px; height: 400px; }
  .badge-new {
    position: absolute; left: 120px; top: 33px; width: 184px; height: 184px;
    border-radius: 50%; background: var(--white);
  }
  .badge-new__label {
    position: absolute; left: 100px; top: 92px; width: 230px;
    font-family: "Montserrat", Arial, sans-serif; font-weight: 800; font-size: 66px;
    line-height: 1; color: var(--teal); text-align: center;
    transform: rotate(-30deg);
    -webkit-text-stroke: 10px var(--white); paint-order: stroke fill;
  }
  .headline {
    position: absolute; left: 328px; top: 30px; margin: 0;
    font-family: "Montserrat", Arial, sans-serif; font-weight: 800;
    font-size: 106px; line-height: 88px; color: var(--white); letter-spacing: 1px;
  }
  .headline span { display: block; }
  .headline .line-2 { padding-left: 16px; }
  .tagline {
    position: absolute; right: 142px; top: 245px; margin: 0; text-align: right;
    font-family: "Montserrat", Arial, sans-serif; font-weight: 700;
    font-size: 29px; line-height: 37px; color: var(--white); letter-spacing: 0.5px;
  }
  .support-icon { position: absolute; left: 86px; top: 410px; width: 94px; height: 84px; }
  .services-label {
    position: absolute; left: 30px; top: 503px; width: 210px; margin: 0; text-align: center;
    font-weight: 700; font-size: 31px; line-height: 35px; letter-spacing: 2.5px; color: var(--ink);
  }
  .services {
    position: absolute; left: 258px; top: 372px; margin: 0; padding: 0; list-style: none;
    font-size: 30.5px; line-height: 35px; letter-spacing: 0.6px; color: var(--ink);
  }
  .services li { white-space: nowrap; }
  .services li::before {
    content: ""; display: inline-block; width: 13px; height: 13px; border-radius: 50%;
    background: var(--ink); margin: 0 14px 5px 2px; vertical-align: middle;
  }
  .photo-team {
    position: absolute; left: 0; top: 648px; width: 540px; height: 362px;
    background:
      linear-gradient(180deg, rgba(241,243,244,1) 0%, rgba(241,243,244,0) 22%),
      linear-gradient(90deg, #f6f6f6 0%, #e8d5c8 10%, #f2f4f6 20%, #6fa9dc 34%, #dcc4b4 42%,
        #8ec3ea 55%, #6aa7dc 72%, #5d9fd8 86%, #e7ecf0 100%);
  }
  .photo-care {
    position: absolute; left: 470px; top: 548px; width: 500px; height: 500px; z-index: 2;
    border-radius: 50%; border: 8px solid var(--white); box-sizing: border-box;
    background:
      radial-gradient(circle at 74% 48%, #ead6ca 0%, #e6cfc2 14%, rgba(230,207,194,0) 30%),
      radial-gradient(circle at 70% 82%, #f2d9de 0%, #e9c6cd 16%, rgba(233,198,205,0) 34%),
      radial-gradient(circle at 30% 30%, #e8cf9e 0%, rgba(232,207,158,0) 28%),
      linear-gradient(135deg, #dfe6ea 0%, #6fa5d4 35%, #7d8a8e 70%, #b9b9b4 100%);
  }
  .contact-band {
    position: absolute; left: 0; top: 1010px; width: 928px; height: 190px;
    background: var(--band); border-top: 5px solid var(--teal); box-sizing: border-box;
  }
  .booking {
    position: absolute; left: 0; top: 1065px; width: 928px; margin: 0; text-align: center;
    font-size: 32px; line-height: 38px; color: var(--white); z-index: 3;
  }
  .booking strong { font-weight: 700; letter-spacing: 1px; }
  .address {
    position: absolute; left: 0; top: 1153px; width: 928px; margin: 0; text-align: center;
    font-family: "Questrial", Verdana, sans-serif; font-size: 25px; letter-spacing: 0.3px;
    color: var(--address); z-index: 3; white-space: nowrap;
  }
</style>
</head>
<body>
<main class="flyer">
  <svg class="header-waves" viewBox="0 0 928 400" aria-hidden="true">
    <defs>
      <linearGradient id="tealFill" x1="0" y1="0" x2="1" y2="1">
        <stop offset="0" stop-color="#36c8d6"/>
        <stop offset="1" stop-color="#13a9b6"/>
      </linearGradient>
    </defs>
    <path d="M0,170 C150,250 350,330 560,350 C700,362 830,340 928,300 V330 C820,370 680,380 540,370 C340,352 160,290 0,240 Z" fill="#bfeff3"/>
    <path d="M0,0 H928 V300 C820,345 690,362 550,352 C350,338 170,268 0,205 Z" fill="url(#tealFill)"/>
    <path d="M0,205 C170,268 350,338 550,352 C690,362 820,345 928,300 V318 C820,360 690,372 548,362 C350,348 170,282 0,222 Z" fill="var(--teal-deep)"/>
  </svg>

  <div class="badge-new"></div>
  <div class="badge-new__label">NEW</div>
  <h1 class="headline"><span class="line-1">MEDICAL</span><span class="line-2">CLINIC</span></h1>
  <p class="tagline">ACCEPTING WALK-IN PATIENTS<br>OPEN 6 DAYS A WEEK</p>

  <svg class="support-icon" viewBox="0 0 94 84" aria-hidden="true">
    <path d="M12,50 V40 C12,18 28,4 47,4 C66,4 82,18 82,40 V50" fill="none" stroke="#111" stroke-width="7"/>
    <rect x="4" y="36" width="16" height="24" rx="6" fill="#111"/>
    <rect x="74" y="36" width="16" height="24" rx="6" fill="#111"/>
    <path d="M20,58 C26,74 40,78 52,78" fill="none" stroke="#111" stroke-width="5"/>
    <rect x="48" y="73" width="12" height="9" rx="3" fill="#111"/>
  </svg>
  <p class="services-label">SERVICES<br>INCLUDES</p>

  <ul class="services">
    <li>Family Practice</li>
    <li>Cardiology Diagnostics</li>
    <li>Cardiac &amp; Vascular Surgical Consultation</li>
    <li>Ultrasound &amp; Vascular Testing</li>
    <li>Open 6 days a week.</li>
    <li>Ample Free Parking</li>
    <li>Friendly Staffs</li>
  </ul>

  <div class="photo-team" role="img" aria-label="Photo of a smiling medical team of four doctors and nurses in white coats and blue scrubs"></div>
  <div class="contact-band"></div>
  <div class="photo-care" role="img" aria-label="Photo of a nurse in blue scrubs comforting a smiling elderly woman in a pink blouse and grey cardigan"></div>

  <p class="booking">TO BOOK APPOINTMENT,<br>PLEASE CALL <strong>(555) 384-2760</strong></p>
  <p class="address">2957 Corliss Road West, Unit 418, Scarborough, Ontario, K7P 2H9</p>
</main>
</body>
</html>
```